established lighting store -latest lighting designs

I would like a design for a 2 sided brochure (front and back) A4
I own a lighting store and have been servicing and supplying lights for 16 years
We supply lighting to over 100 builders
We work with designers ,architects, home renovators
We have the latest designs and trends in lighting
We offer personalised service to all our customers
We can help you with the lighting design of your new home or commercial project

We currently supply lights to about 20 builders who have display homes in a display village nearby http://dwellorbit.com.au
These display homes have potential buyers of the homes walking through them and therefore potential customers of ours.
Usually the builder will refer the client to us but it would be nice to have some kind of presence in the display home in the way of a brochure.
This will enable us to possibly pick up client who are just browsing thru the homes

I'd the photos to do most of the talking with a description similar to the brochure attached .(which says "at nexar lighting pembry vale we excel......) PLEASE NOTE COMPANY NAME IS NOW
NEXAR LIGHTING PEMBRY VALE

we will need
company name NEXAR LIGHTING PEMBRY VALE
logo ATTACHED
address UNIT 27 / 4 MARLOWE ST , PEMBRY VALE
phone no 97418305

and an invitation to come into our showroom with their plans to help them with their lighting layout and to help them select the right lighting for their home

i like the idea of black background with the photos overlaping with border around each
photos can be cropped to suit

some sample black background brochures attached

Target Market(s)

NEW HOME OWNERS BUILDING NEW HOMES NEEding lights
builders clients
renovators

Industry/Entity Type

Store

Font styles to use
Sans Serif

Colors
000000
5c5c5c
606060
fbed22
ec1f27
0255a3
00a990
9bcb3c
f37122

Requirements
Must have
• black background
• pictures to be the main focus
• short write up on our services and invitation to visit our store
Nice to have
• please note we are not
• nexar lighting pembry vale (as per some of the previous ads)
• we are now
• nexar light pembry vale
• ++++++++++++++++++++++++++++
• from some wording from our competitors websites
• """"""Nexar Lighting Pembry Vale is the newest and most distinctive destination for lighting in Sydney. We pride ourselves on sourcing both unique and accessible products with a range that will continue to evolve as new designs and options become available.
• Our service is personalised, and we aim to assist your design choices; be it feature lights in Willoughby, functional lights in Annandale, or an entire home lighting solution.
• Offering a fresh approach to interior and exterior designer lighting in Annandale and Willoughby, our display range includes distinct style European imports through to products that are sourced and manufactured locally. It is our intention to bring together a select range of high quality items to meet the discerning customer’s taste and practical requirements.""""""
• """"""""Here at Nexar Lighting Pembry Vale, we have been creating light for over 40 years. Our professional staff, including interior designers and electrical engineers can creatively respond to aesthetic and functional issues with a clear focus on client satisfaction. We are a full-service lighting destination, offering expert advice in layout and design as well as comprehensive style guidance. We are authorised lighting partners with some of the world’s most prestigious and exclusive lighting manufacturers, showcased in our ever-evolving showroom."""
• """Responding to local trends as well as emerging European concepts, we offer an abundance of individual and creative possibilities with an extensive range of contemporary and traditional fittings. We specialise in everything from period restorations to cutting-edge modern and with thousands of stock items, inspiration is never far away. We are truly passionate about light. Come and see why we are different. Call or drop in today or take advantage of our appointment service at Australia’s premiere lighting destination.""""

```html
<!DOCTYPE html>
<html lang="en">
<head>
<meta charset="utf-8">
<title>Nexar Lighting Pembry Vale – Brochure</title>
<link rel="stylesheet" href="https://fonts.googleapis.com/css2?family=Open+Sans:wght@400;600;700;800&display=swap">
<style>
  :root {
    --canvas-bg: #d9d9d9;
    --sheet-dark: #3d3c3c;
    --text-light: #f2f2f2;
    --logo-ink: #2f2f2f;
    --brand-blue: #0255a3;
    --frame: #ffffff;
    --shadow: rgba(0,0,0,0.35);
  }
  * { box-sizing: border-box; margin: 0; padding: 0; }
  html, body { width: 1200px; height: 960px; overflow: hidden; }
  body {
    background: var(--canvas-bg);
    font-family: "Open Sans", Arial, sans-serif;
    position: relative;
  }
  .sheet {
    position: absolute;
    top: 266px;
    width: 570px;
    height: 428px;
    overflow: hidden;
    box-shadow: 0 6px 18px var(--shadow);
  }
  .sheet--front { left: 20px; }
  .sheet--back { left: 610px; background: var(--sheet-dark); }

  /* Front */
  .front-photo {
    position: absolute; inset: 0;
    background:
      linear-gradient(180deg,
        #a9a8a6 0%, #c2c1bf 38%, #d8dde2 46%,
        #f4f8fb 52%, #eef3f7 58%, #cfd3d6 62%,
        #7a7068 63%, #6b625a 80%, #5e5650 100%);
  }
  .logo {
    position: absolute;
    left: 365px; top: 178px;
    display: flex; align-items: center; gap: 6px;
  }
  .logo__mark { width: 10px; height: 10px; background: var(--brand-blue); }
  .logo__name {
    color: var(--logo-ink);
    font-weight: 700;
    font-size: 12px;
    line-height: 1.05;
    letter-spacing: 0.2px;
  }
  .headline {
    position: absolute;
    left: 300px; top: 290px; width: 250px;
    color: #ffffff;
    font-weight: 800;
    font-size: 19px;
    line-height: 1.12;
    text-align: center;
  }
  .contact {
    position: absolute;
    left: 50px; top: 356px;
    color: #ffffff;
    text-align: center;
    font-size: 8.5px;
    line-height: 1.35;
  }
  .contact__label { font-weight: 400; font-size: 10px; letter-spacing: 0.3px; }
  .contact__line { font-weight: 700; }

  /* Back */
  .photo {
    position: absolute;
    border: 3px solid var(--frame);
    border-radius: 4px;
    box-shadow: 0 3px 8px rgba(0,0,0,0.5);
  }
  .photo--ceiling { left: 18px;  top: 96px;  width: 120px; height: 92px;  background: linear-gradient(160deg,#f3f0ea,#bfb7a8 55%,#8a7d6a); transform: rotate(3deg); }
  .photo--disc    { left: 128px; top: 86px;  width: 110px; height: 84px;  background: radial-gradient(ellipse at 50% 60%,#f7f2e6,#c9c1b1 60%,#7c7466); transform: rotate(2deg); }
  .photo--crystal { left: 228px; top: 70px;  width: 96px;  height: 140px; background: linear-gradient(180deg,#3a3a3a,#9a9a96 45%,#d9d8d2 60%,#6c6c68); transform: rotate(-2deg); }
  .photo--pendant { left: 296px; top: 8px;   width: 112px; height: 120px; background: radial-gradient(ellipse at 45% 40%,#ffb060,#d4621c 45%,#3a1a0c 90%); transform: rotate(-4deg); }
  .photo--house   { left: 396px; top: 44px;  width: 130px; height: 112px; background: linear-gradient(180deg,#d9866a 0%,#8a7fa0 40%,#e7eaee 62%,#8d9aa8 100%); transform: rotate(3deg); }
  .photo--silver  { left: 420px; top: 146px; width: 132px; height: 82px;  background: radial-gradient(ellipse at 50% 50%,#f2f2f2,#a4a4a4 55%,#2c2c2c); transform: rotate(2deg); }

  .copy {
    position: absolute;
    top: 240px; left: 22px; right: 22px;
    display: flex; gap: 26px;
    color: var(--text-light);
    font-size: 6.6px;
    line-height: 1.38;
  }
  .copy__col { flex: 1; }
  .copy__col p { margin-bottom: 4px; }
</style>
</head>
<body>

  <section class="sheet sheet--front" aria-label="Brochure front">
    <div class="front-photo" role="img" aria-label="Photo of a modern kitchen with grey overhead cabinets, a glowing under-cabinet light strip and taupe lower cabinets"></div>

    <div class="logo">
      <span class="logo__mark"></span>
      <span class="logo__name">NEXAR LIGHTING<br>PEMBRY VALE</span>
    </div>

    <h1 class="headline">16 YEARS OF<br>GOOD OLD FASHIONED<br>CUSTOMER SERVICE</h1>

    <div class="contact">
      <p class="contact__label">CONTACT US</p>
      <p class="contact__line">UNIT 27 / 4 MARLOWE ST , PEMBRY VALE</p>
      <p class="contact__line">Phone No.: 97418305</p>
    </div>
  </section>

  <section class="sheet sheet--back" aria-label="Brochure back">
    <div class="photo photo--ceiling" role="img" aria-label="Photo of a lit ceiling in a living room"></div>
    <div class="photo photo--disc" role="img" aria-label="Photo of a large disc ceiling light"></div>
    <div class="photo photo--crystal" role="img" aria-label="Photo of a cascading crystal chandelier"></div>
    <div class="photo photo--pendant" role="img" aria-label="Photo of glowing orange drum pendant lights"></div>
    <div class="photo photo--house" role="img" aria-label="Photo of a modern house lit at dusk"></div>
    <div class="photo photo--silver" role="img" aria-label="Photo of a silver draped chandelier"></div>

    <div class="copy">
      <div class="copy__col">
        <p>Nexar Lighting Pembry Vale is an established and distinctive destination for lighting in Sydney. We pride ourselves on sourcing both unique and accessible products with a range that will continue to evolve as new designs and options become available.</p>
        <p>Our service is personalised, and we aim to assist your design choices, be it feature lights, functional lights, or an entire home lighting solution for your new home or commercial project.</p>
        <p>Offering a fresh approach to interior and exterior designer lighting, our display range includes distinct style European imports through to products that are sourced and manufactured locally. We supply over 100 builders and work with designers, architects and home renovators to meet the discerning customer’s taste and practical requirements.</p>
      </div>
      <div class="copy__col">
        <p>Here at Nexar Lighting Pembry Vale, we have been servicing and supplying lights for 16 years. Our professional staff can creatively respond to aesthetic and functional issues with a clear focus on client satisfaction. We are a full-service lighting destination, offering expert advice in layout and design as well as comprehensive style guidance, showcased in our ever-evolving showroom.</p>
        <p>Responding to local trends as well as emerging European concepts, we offer an abundance of individual and creative possibilities with an extensive range of contemporary and traditional fittings. Bring your plans into our showroom and we will help you with your lighting layout and help you select the right lighting for your home. Come and see why we are different. Call or drop in today.</p>
      </div>
    </div>
  </section>

</body>
</html>
```